Unique and original Business Card for Financial Services Business

I have moved premises and need to change the detail on my business card so thought now is a good time for a re-design. Looking for something professional and modern with colours to fit in with out logo. Like the idea of foil or embossing if that works but not a must have but I do want something that stands out and that I could not design myself.

Once business card is designed I will also be looking to get letterhead and flyers done but want the business card concept in place first.

The majority of designs I am receiving are generic and template based. I am looking for something unique and original. We have some great design elements in our logo, think outside the box and show me something that stands out from the crowd.

Target Market(s)

Business Professionals

Industry/Entity Type

Finance

Contact Information for Business Card

Name: Delia Norwood Phone 0473 958 162 Address PO Box 8617 Mossvale NSW 2389 Email info@steadyharbourfinancialservices.com.au website www.steadyharbourfinancialservices.com.au

Font styles to use
Other font styles liked:
• Ralway

Requirements
Should not have
• No black backgrounds please

```html
<!DOCTYPE html>
<html lang="en">
<head>
<meta charset="utf-8">
<title>Steady Harbour Financial Services – Business Card</title>
<link rel="stylesheet" href="https://fonts.googleapis.com/css2?family=Montserrat:wght@400;500;700&display=swap">
<style>
  :root {
    --backdrop: #939393;
    --card-white: #ffffff;
    --teal: #1a8f97;
    --teal-bright: #0a9aa0;
    --teal-deep: #003a5c;
    --ink: #222222;
    --motif-light: #f1f2f2;
  }
  * { box-sizing: border-box; margin: 0; padding: 0; }
  html, body {
    width: 1200px; height: 1056px; overflow: hidden;
    background: var(--backdrop);
    font-family: "Montserrat", sans-serif;
  }
  .stage { position: relative; width: 1200px; height: 1056px; }

  .card {
    position: absolute;
    width: 620px; height: 354px;
    overflow: hidden;
    box-shadow: 0 12px 28px rgba(0,0,0,0.25);
  }

  /* Front */
  .card--front { left: 110px; top: 110px; background: var(--card-white); }
  .card--front .motif {
    position: absolute; right: 0; top: 0; width: 300px; height: 354px;
    background: radial-gradient(ellipse at 60% 55%, var(--motif-light) 0%, rgba(241,242,242,0.4) 55%, rgba(255,255,255,0) 80%);
  }
  .brand {
    position: absolute; left: 56px; top: 52px;
    color: var(--teal); font-weight: 500; line-height: 1.15;
    display: flex; align-items: center; gap: 12px;
  }
  .brand__dot { width: 34px; height: 34px; border-radius: 50%; background: var(--teal); }
  .brand__name { font-size: 20px; letter-spacing: 0.06em; text-transform: uppercase; }
  .brand__name small { display: block; font-size: 12px; letter-spacing: 0.32em; }
  .holder {
    position: absolute; left: 56px; top: 146px;
    color: var(--teal); font-weight: 700; font-size: 30px;
    letter-spacing: 0.04em; text-transform: uppercase;
  }
  .contacts { position: absolute; left: 56px; top: 204px; list-style: none; }
  .contacts li {
    display: flex; align-items: center; gap: 8px;
    font-size: 12.5px; color: var(--ink); margin-bottom: 9px;
  }
  .contacts svg { width: 15px; height: 15px; flex: none; }

  /* Back */
  .card--back {
    left: 470px; top: 580px;
    background: linear-gradient(225deg, var(--teal-bright) 0%, #006e84 50%, var(--teal-deep) 100%);
  }
  .card--back .motif {
    position: absolute; inset: 0;
    background: radial-gradient(ellipse at 30% 45%, rgba(0,0,0,0.12) 0%, rgba(0,0,0,0) 55%),
                radial-gradient(ellipse at 80% 60%, rgba(255,255,255,0.06) 0%, rgba(255,255,255,0) 50%);
  }
  .brand--back {
    position: absolute; left: 0; right: 0; top: 0; bottom: 0;
    display: flex; flex-direction: column; align-items: center; justify-content: center; gap: 14px;
    color: #ffffff; font-weight: 500; text-transform: uppercase; text-align: center;
  }
  .brand--back .brand__dot { width: 60px; height: 60px; background: #ffffff; }
  .brand--back .brand__name { font-size: 28px; letter-spacing: 0.06em; line-height: 1.2; }
  .brand--back .brand__name small { font-size: 15px; letter-spacing: 0.4em; }
</style>
</head>
<body>
<main class="stage">

  <section class="card card--front">
    <div class="motif" role="img" aria-label="Faint hummingbird and floral watermark"></div>
    <div class="brand">
      <span class="brand__dot"></span>
      <span class="brand__name">Steady Harbour<small>Financial Services</small></span>
    </div>
    <h1 class="holder">Delia Norwood</h1>
    <ul class="contacts">
      <li>
        <svg viewBox="0 0 16 16"><circle cx="8" cy="8" r="8" fill="#1a8f97"/><path d="M5.3 4.5l1.4-.3.8 1.9-.9.7a5 5 0 0 0 2.6 2.6l.7-.9 1.9.8-.3 1.4c-3.4.3-6.5-2.8-6.2-6.2z" fill="#fff"/></svg>
        0473 958 162
      </li>
      <li>
        <svg viewBox="0 0 16 16"><circle cx="8" cy="8" r="8" fill="#1a8f97"/><rect x="4" y="5.2" width="8" height="5.6" rx="0.6" fill="#fff"/><path d="M4.3 5.6L8 8.4l3.7-2.8" stroke="#1a8f97" stroke-width="0.8" fill="none"/></svg>
        info@steadyharbourfinancialservices.com.au
      </li>
      <li>
        <svg viewBox="0 0 16 16"><circle cx="8" cy="8" r="8" fill="#1a8f97"/><circle cx="8" cy="8" r="4" stroke="#fff" stroke-width="0.9" fill="none"/><ellipse cx="8" cy="8" rx="1.7" ry="4" stroke="#fff" stroke-width="0.8" fill="none"/><path d="M4 8h8" stroke="#fff" stroke-width="0.8"/></svg>
        www.steadyharbourfinancialservices.com.au
      </li>
      <li>
        <svg viewBox="0 0 16 16"><circle cx="8" cy="8" r="8" fill="#1a8f97"/><path d="M8 3.5a3 3 0 0 0-3 3c0 2.3 3 6 3 6s3-3.7 3-6a3 3 0 0 0-3-3z" fill="#fff"/><circle cx="8" cy="6.5" r="1.1" fill="#1a8f97"/></svg>
        PO Box 8617 Mossvale NSW 2389
      </li>
    </ul>
  </section>

  <section class="card card--back">
    <div class="motif" role="img" aria-label="Tonal hummingbird and floral pattern"></div>
    <div class="brand brand--back">
      <span class="brand__dot"></span>
      <span class="brand__name">Steady Harbour<small>Financial Services</small></span>
    </div>
  </section>

</main>
</body>
</html>
```